The Quiet Harbor

I have a faux cover I will attach & want you to follow & enhance what I've created. Just an FYI, the book will be posted on brindlo & I'm working with Marrow Lane Publishing.
What you need to know:
The dimensions: 6" x 9" (15.24 x 22.86 cm)
Background color: Black
I did not capture the color of the font, so want you to get a similar gold color.
Font for title, subtitle & author name: Goudy Old Style
Font for "20th Anniversary Edition": Kunstler Script
I have thoughts of shaping the photo in an oval shape -- possibly shade out the edges?

Target Market(s)

All ages: anyone who has encountered issues with doctors, hospitals, and especially those who have struggled with cancer treatment.

Requirements
Nice to have
• Adding below another PDF, showing vintage lines that I would like to see used. Just added some text I will add to the back cover. I am waiting on one more review, which I will add. Attaching that below.

```html
<!DOCTYPE html>
<html lang="en">
<head>
<meta charset="utf-8">
<title>The Quiet Harbor – Book Cover</title>
<link href="https://fonts.googleapis.com/css2?family=Sorts+Mill+Goudy&family=Pinyon+Script&display=swap" rel="stylesheet">
<style>
  :root {
    --backdrop: #e6c565;
    --cover-black: #050505;
    --gold-light: #f7e7a0;
    --gold-mid: #d9b340;
    --gold-deep: #9c7418;
    --gold-flat: #e3c43e;
    --photo-light: #dcdde2;
    --photo-dark: #5b5c62;
  }
  * { margin: 0; padding: 0; box-sizing: border-box; }
  html, body {
    width: 903px;
    height: 1200px;
    overflow: hidden;
    background: var(--backdrop);
  }
  .canvas {
    position: relative;
    width: 903px;
    height: 1200px;
  }
  .cover {
    position: absolute;
    left: 96px;
    top: 67px;
    width: 711px;
    height: 1065px;
    background: var(--cover-black);
    box-shadow: 0 0 18px rgba(0, 0, 0, 0.45);
  }
  .title {
    position: absolute;
    left: 0;
    top: 77px;
    width: 100%;
    text-align: center;
    font-family: "Sorts Mill Goudy", "Goudy Old Style", serif;
    font-weight: 400;
    text-transform: uppercase;
    line-height: 125px;
    filter: drop-shadow(0 0 6px rgba(255, 215, 120, 0.35));
  }
  .title-line {
    display: block;
    font-size: 112px;
    letter-spacing: 1px;
    background: linear-gradient(180deg, var(--gold-light) 20%, var(--gold-mid) 55%, var(--gold-deep) 85%);
    -webkit-background-clip: text;
    background-clip: text;
    color: transparent;
  }
  .edition {
    position: absolute;
    left: 0;
    top: 312px;
    width: 100%;
    text-align: center;
    font-family: "Pinyon Script", cursive;
    font-size: 58px;
    line-height: 1;
    word-spacing: 6px;
    color: var(--gold-mid);
  }
  .portrait {
    position: absolute;
    left: 163px;
    top: 390px;
    width: 385px;
    height: 541px;
  }
  .author {
    position: absolute;
    left: 0;
    top: 957px;
    width: 100%;
    text-align: center;
    font-family: "Sorts Mill Goudy", "Goudy Old Style", serif;
    font-size: 54px;
    letter-spacing: 1px;
    color: var(--gold-flat);
  }
</style>
</head>
<body>
  <div class="canvas">
    <div class="cover">
      <h1 class="title">
        <span class="title-line">The Quiet</span>
        <span class="title-line">Harbor</span>
      </h1>
      <p class="edition">20th Anniversary Edition</p>
      <svg class="portrait" viewBox="0 0 385 541" xmlns="http://www.w3.org/2000/svg">
        <defs>
          <linearGradient id="frame-gold" x1="0" y1="0" x2="1" y2="1">
            <stop offset="0" stop-color="var(--gold-light)"/>
            <stop offset="0.45" stop-color="var(--gold-mid)"/>
            <stop offset="0.7" stop-color="var(--gold-deep)"/>
            <stop offset="1" stop-color="var(--gold-light)"/>
          </linearGradient>
          <radialGradient id="photo-tone" cx="0.5" cy="0.45" r="0.6">
            <stop offset="0" stop-color="var(--photo-light)"/>
            <stop offset="1" stop-color="var(--photo-dark)"/>
          </radialGradient>
        </defs>
        <ellipse class="portrait-frame" cx="192.5" cy="270.5" rx="190" ry="268" fill="url(#frame-gold)"/>
        <ellipse cx="192.5" cy="270.5" rx="180" ry="258" fill="var(--gold-deep)"/>
        <ellipse class="portrait-photo" cx="192.5" cy="270.5" rx="176" ry="254" fill="url(#photo-tone)" role="img" aria-label="Black and white portrait photograph of the author, smiling, wearing glasses"/>
      </svg>
      <p class="author">AUTHOR NAME</p>
    </div>
  </div>
</body>
</html>
```